Kestrel Homes Australia Business Card

We need a Business Card design for our new start up company.
A unique model designed to address Australia’s growing housing affordability problem has been launched. More than half of Australians are being priced out of the property market and have resigned themselves to the fact that they may never be able to afford a home.
We have developed a unique Algorithm that allows people to get into property and reverse this trend of domination by the property investors in this country. The first of its kind model facilitates connecting people to lending facilities that do not require them to have the finance combined under the purchase contract.
Ownership is shared with a second-tier investor, made up of either family or friends if not, Kestrel Homes Australia will provide a mini property investor enabling thousands of people the opportunity to buy a home, which they otherwise thought was not possible.
Kestrel Homes Australia is addressing housing affordability for families and individuals, giving every Australian looking to buy a home the opportunity to enter the property market to live in or invest.
Under our unique model, there is no combined finance, and individuals are assessed for their percentage portion of the property only. “A unique feature of our product is it is based around the strategies used for property investment. I have developed a unique Algorithm that enables the Home buyer to purchase 60% of a property, while Kestrel Homes Australia facilitates a second-tier investor to buy the other 40%. The Algorithm locks the investor in place and enables the home buyer to stairway to full ownership. The investment is secured against real property.
Please refer to our website www.kestrelhomes.com.au for inspiration.
Also please find attached our logo.
Any further directions please ask.
Cheers Marcus
Industry/Entity Type
Real Estate
Contact Information for Business Card
Marcus Thorley
CEO
Mobile 0400 615 272
www.kestrelhomes.com.au
Email: marcus@kestrelhomes.com.au
Colors
Designer to choose colors to be used in the design.
Look and feel

```html
<!DOCTYPE html>
<html lang="en">
<head>
<meta charset="utf-8">
<title>Kestrel Homes Australia – Business Card</title>
<link href="https://fonts.googleapis.com/css2?family=Montserrat:wght@400;500;700&display=swap" rel="stylesheet">
<style>
  :root{
    --stage:#3b3430;
    --card:#151515;
    --blue:#1ea6d9;
    --green:#3aa845;
    --foil:#8a8a8a;
  }
  html,body{margin:0;padding:0;overflow:hidden;}
  body{width:1200px;height:780px;background:var(--stage);font-family:"Montserrat",sans-serif;position:relative;}
  .card{position:absolute;width:520px;height:300px;background:var(--card);border-radius:4px;box-shadow:0 18px 40px rgba(0,0,0,.55);}
  .card--back{left:60px;top:150px;}
  .card--front{left:620px;top:330px;}

  .back-mark{position:absolute;left:0;right:0;top:128px;text-align:center;color:var(--foil);font-weight:700;font-size:22px;letter-spacing:.5px;white-space:nowrap;}
  .back-mark .dot{display:inline-block;width:14px;height:14px;border-radius:50%;background:var(--foil);margin-right:10px;vertical-align:middle;}

  .brand{position:absolute;right:34px;top:62px;text-align:right;white-space:nowrap;}
  .brand__name{color:var(--blue);font-weight:700;font-size:30px;line-height:1;}
  .brand__tagline{color:var(--green);font-weight:500;font-size:14px;margin-top:8px;}

  .person{position:absolute;left:24px;top:186px;width:160px;text-align:right;white-space:nowrap;}
  .person__name{color:var(--blue);font-weight:700;font-size:17px;line-height:1.2;}
  .person__role{color:var(--green);font-weight:400;font-size:14px;margin-top:2px;}

  .divider{position:absolute;left:198px;top:180px;width:2px;height:78px;background:var(--green);}

  .contacts{position:absolute;left:216px;top:182px;list-style:none;margin:0;padding:0;white-space:nowrap;}
  .contacts li{display:flex;align-items:center;height:24px;color:var(--blue);font-size:14px;font-weight:400;}
  .contacts svg{width:16px;height:16px;margin-right:9px;flex:none;}
</style>
</head>
<body>
  <div class="card card--back">
    <div class="back-mark"><span class="dot"></span>Kestrel Homes Australia</div>
  </div>

  <div class="card card--front">
    <div class="brand">
      <div class="brand__name">Kestrel Homes Australia</div>
      <div class="brand__tagline">Opening Doors to Home Ownership</div>
    </div>

    <div class="person">
      <div class="person__name">Marcus Thorley</div>
      <div class="person__role">CEO</div>
    </div>

    <div class="divider"></div>

    <ul class="contacts">
      <li>
        <svg viewBox="0 0 16 16" aria-hidden="true"><rect width="16" height="16" rx="2" fill="#3aa845"/><rect x="5" y="2.5" width="6" height="11" rx="1" fill="none" stroke="#151515" stroke-width="1.4"/><circle cx="8" cy="11.5" r=".8" fill="#151515"/></svg>
        0400 615 272
      </li>
      <li>
        <svg viewBox="0 0 16 16" aria-hidden="true"><rect width="16" height="16" rx="2" fill="#3aa845"/><rect x="3" y="4.5" width="10" height="7" fill="none" stroke="#151515" stroke-width="1.3"/><path d="M3 4.5 8 9l5-4.5" fill="none" stroke="#151515" stroke-width="1.3"/></svg>
        marcus@kestrelhomes.com.au
      </li>
      <li>
        <svg viewBox="0 0 16 16" aria-hidden="true"><rect width="16" height="16" rx="2" fill="#3aa845"/><circle cx="8" cy="8" r="5" fill="none" stroke="#151515" stroke-width="1.2"/><ellipse cx="8" cy="8" rx="2.2" ry="5" fill="none" stroke="#151515" stroke-width="1.1"/><path d="M3 8h10" stroke="#151515" stroke-width="1.1"/></svg>
        www.kestrelhomes.com.au
      </li>
    </ul>
  </div>
</body>
</html>
```